Mabiboo creole shop needs a web design

We need a web design former new company based in sydney australia. Called 'Mabiboo, creole shop'.
We produce caribbean/west indies product alcohol, spirits, condiments, candies, preserved food, jams, pates.
We would like to see a design that reflect the caribbean without being tacky.
We want modern, high level design as we do high level products.

Reason: There is a lot of good proposition but I need a few more days to mature my decision. Thanks for your hard work Jorel

Industry/Entity Type

Hospitality

Number of Pages Required

1 page

Font styles to use
Decorative
Script

Requirements
Must have
• The logo, the name of the business

```html
<!DOCTYPE html>
<html lang="en">
<head>
<meta charset="utf-8">
<title>Mabiboo creole shop</title>
<link rel="stylesheet" href="https://fonts.googleapis.com/css2?family=Dancing+Script:wght@500;700&family=Quicksand:wght@400&display=swap">
<style>
:root{
  --navy:#1f2b5e;
  --gold:#c1a12c;
  --gold-soft:#ccb03a;
  --white:#ffffff;
  --backdrop:#1b1712;
  --ink:#2a2a2a;
  --muted:#6d6d6d;
  --script:"Dancing Script", cursive;
  --sans:"Quicksand", sans-serif;
  --body:Arial, Helvetica, sans-serif;
}
*{box-sizing:border-box;margin:0;padding:0}
html,body{width:832px;height:1200px;overflow:hidden}
body{background:var(--backdrop);position:relative;font-family:var(--body)}
.page{position:absolute;left:112px;top:25px;width:608px;background:var(--white)}
.masthead{display:flex;height:280px}
.brand-col{width:179px;display:flex;flex-direction:column}
.brand{height:162px;display:flex;flex-direction:column;align-items:center;justify-content:center;gap:8px}
.brand-mark{width:18px;height:18px;border-radius:50%;background:var(--gold)}
.brand-name{font-family:var(--script);font-weight:700;font-size:34px;color:var(--navy);line-height:1}
.brand-sub{font-family:var(--script);font-weight:700;font-size:14px;color:var(--navy)}
.tagline{flex:1;background:var(--gold);color:var(--white);font-family:var(--sans);text-align:center;display:flex;flex-direction:column;justify-content:center;line-height:1.2}
.tagline .l1{font-size:24px}
.tagline .l2{font-size:19px}
.tagline .l3{font-size:24px}
.hero{flex:1;position:relative;background:radial-gradient(ellipse at 35% 35%,#c99a1c 0%,#7a4a10 45%,#2a1608 85%)}
.dots{position:absolute;right:16px;bottom:13px;display:flex;gap:3px}
.dots span{width:7px;height:7px;border-radius:50%;background:var(--white)}
.dots span:first-child{background:var(--gold)}
.main-nav{height:42px;background:var(--navy);display:flex;justify-content:center;align-items:center;gap:12px;font-family:var(--script);font-weight:500;font-size:15px;color:var(--white)}
.main-nav .sep{opacity:.8}
.main-nav .active{color:var(--gold);text-decoration:underline}
.about{height:189px;text-align:center;padding-top:44px}
.section-title{font-family:var(--script);font-weight:700;font-size:20px}
.about .section-title{color:var(--navy)}
.about p{width:372px;margin:14px auto 0;text-align:left;font-style:italic;font-size:7.6px;line-height:12.5px;color:var(--ink)}
.products{height:409px;background:var(--navy);text-align:center;padding-top:36px;position:relative}
.products .section-title{color:var(--white)}
.tabs{display:flex;justify-content:center;gap:3px;margin-top:28px}
.tabs span{background:var(--gold);color:var(--white);font-family:var(--script);font-weight:500;font-size:13px;height:22px;line-height:22px;padding:0 6px}
.tabs .active{background:var(--white);color:var(--navy)}
.cards{position:absolute;left:16px;top:132px;display:flex;gap:14px}
.card{width:104px;text-align:center}
.card-frame{height:165px;background:var(--white);border:1px solid var(--gold);display:flex;align-items:center;justify-content:center}
.bottle{width:34px;height:136px;border-radius:14px 14px 6px 6px}
.card-label{margin-top:16px;font-family:var(--script);font-weight:500;font-size:14px;color:var(--white)}
.view-all{position:absolute;left:192px;top:358px;width:224px;display:flex;align-items:center;gap:8px;font-style:italic;font-size:8px;color:var(--gold)}
.view-all i{flex:1;height:1px;background:var(--gold)}
.engage{height:110px;background:var(--gold);display:flex;position:relative}
.newsletter{width:386px;padding:18px 0 0 26px;border-right:1px solid rgba(0,0,0,.12);margin:18px 0 18px;padding-top:0}
.engage .section-title{color:var(--white);font-size:18px}
.signup{display:flex;margin-top:14px}
.signup .field{width:237px;height:29px;background:var(--gold-soft);border:1px solid #d9c064;font-style:italic;font-size:7.5px;color:#efe2a8;line-height:27px;padding-left:9px}
.signup .btn{width:62px;height:29px;background:var(--white);color:var(--navy);font-family:var(--script);font-weight:700;font-size:12px;line-height:29px;text-align:center}
.follow{flex:1;padding:18px 0 0 56px}
.socials{display:flex;gap:14px;margin-top:14px}
.socials span{width:22px;height:22px;border-radius:50%;border:2px solid var(--white)}
.site-footer{height:107px;text-align:center;padding-top:23px}
.footer-links{display:flex;justify-content:center;gap:6px;font-style:italic;font-size:7.4px;color:var(--navy)}
.footer-links .sep{color:var(--gold)}
.footer-mark{width:16px;height:16px;border-radius:50%;background:var(--gold);margin:18px auto 0}
.footer-brand{font-family:var(--script);font-weight:700;font-size:14px;color:var(--navy);margin-top:3px}
.copyright{font-style:italic;font-size:7.4px;color:var(--muted);margin-top:4px}
</style>
</head>
<body>
<div class="page">
  <header class="masthead">
    <div class="brand-col">
      <div class="brand">
        <span class="brand-mark"></span>
        <span class="brand-name">Mabiboo</span>
        <span class="brand-sub">creole shop</span>
      </div>
      <div class="tagline">
        <span class="l1">The Best</span>
        <span class="l2">Caribbean</span>
        <span class="l3">Creole Shop</span>
      </div>
    </div>
    <div class="hero" role="img" aria-label="Photo of wine bottles, glasses of red and white wine, grapes and a wooden barrel">
      <div class="dots"><span></span><span></span><span></span></div>
    </div>
  </header>

  <nav class="main-nav">
    <span class="active">Home</span><span class="sep">/</span>
    <span>History</span><span class="sep">/</span>
    <span>Products</span><span class="sep">/</span>
    <span>Wholesale &amp; Special Events</span><span class="sep">/</span>
    <span>News</span><span class="sep">/</span>
    <span>Contact</span>
  </nav>

  <section class="about">
    <h2 class="section-title">About Us</h2>
    <p>Lorem ipsum dolor sit amet, consectetur adipiscing elit, sed do eiusmod tempor incididunt ut labore et dolore magna aliqua. Ut enim ad minim veniam, quis nostrud exercitation ullamco laboris nisi ut aliquip ex ea commodo consequat. Duis aute irure dolor in reprehenderit in voluptate velit esse cillum dolore eu fugiat nulla pariatur. Excepteur sint occaecat cupidatat non proident, sunt in culpa qui officia deserunt mollit anim id est laborum.</p>
  </section>

  <section class="products">
    <h2 class="section-title">Our Products</h2>
    <div class="tabs">
      <span class="active">Alcohol</span><span>Spirits</span><span>Condiments</span><span>Candies</span><span>Preserved Food</span><span>Jams</span><span>Pates</span>
    </div>
    <div class="cards">
      <div class="card"><div class="card-frame"><div class="bottle" role="img" aria-label="Photo of a rosé champagne bottle" style="background:linear-gradient(180deg,#d66a7a,#f2a9a4)"></div></div><div class="card-label">Champagne</div></div>
      <div class="card"><div class="card-frame"><div class="bottle" role="img" aria-label="Photo of a dry white wine bottle" style="background:linear-gradient(180deg,#2b2b2b 12%,#e5e4b8 12%,#2a2a2a 60%)"></div></div><div class="card-label">Dry Wine</div></div>
      <div class="card"><div class="card-frame"><div class="bottle" role="img" aria-label="Photo of a semi-dry rosé wine bottle" style="background:linear-gradient(180deg,#d9c08f,#f2b58a 50%,#d6cfba)"></div></div><div class="card-label">Semi-Dry Wine</div></div>
      <div class="card"><div class="card-frame"><div class="bottle" role="img" aria-label="Photo of a dessert red wine bottle" style="background:linear-gradient(180deg,#b3121c 12%,#2a0c12 12%,#1a0a10)"></div></div><div class="card-label">Dessert Wine</div></div>
      <div class="card"><div class="card-frame"><div class="bottle" role="img" aria-label="Photo of a strong white wine bottle" style="background:linear-gradient(180deg,#2b2b2b 12%,#e8e6b0 12%,#222 55%)"></div></div><div class="card-label">Strong Wine</div></div>
    </div>
    <div class="view-all"><i></i><span>view all ...</span><i></i></div>
  </section>

  <section class="engage">
    <div class="newsletter">
      <h2 class="section-title">Newsletter Signup</h2>
      <div class="signup"><span class="field">Enter your email ...</span><span class="btn">Signup</span></div>
    </div>
    <div class="follow">
      <h2 class="section-title">Follow Us</h2>
      <div class="socials" aria-label="Social links"><span></span><span></span><span></span><span></span></div>
    </div>
  </section>

  <footer class="site-footer">
    <div class="footer-links">
      <span>About Us</span><span class="sep">/</span><span>Delivery Information</span><span class="sep">/</span><span>Privacy Policy</span><span class="sep">/</span><span>Terms &amp; Conditions</span><span class="sep">/</span><span>Customer Service</span><span class="sep">/</span><span>Contact Us</span><span class="sep">/</span><span>Returns</span><span class="sep">/</span><span>Site Map</span>
    </div>
    <div class="footer-mark"></div>
    <div class="footer-brand">Mabiboo</div>
    <div class="copyright">Mabiboo, Creole Shop © 2015 All Rights Reserved</div>
  </footer>
</div>
</body>
</html>
```